VR Business Card

Design new business cards for VELMOsoft

Please see attached for the design brief

**** Please note, please feel free to propose a font that works for a professional, technology company ***

Target Market(s)

Technology buyers

Industry/Entity Type

Business

```html
<!DOCTYPE html>
<html lang="en">
<head>
<meta charset="utf-8">
<title>VELMOsoft Business Cards</title>
<link href="https://fonts.googleapis.com/css2?family=Arimo:wght@400;700&display=swap" rel="stylesheet">
<style>
  :root {
    --backdrop: #8a8a88;
    --card-dark: #0c1a22;
    --card-light: #f4f4f4;
    --navy: #2a3a7c;
    --ink: #2b2b2b;
    --tag-grey: #555555;
    --accent-orange: #e8a020;
    --accent-blue: #4a6cc0;
    --accent-green: #146a5a;
    --accent-purple: #5a4aa8;
    --band-start: #0f1a20;
    --band-end: #5f6468;
    --muted-light: #c9cdd0;
    --name-light: #e9ecef;
  }
  * { margin: 0; padding: 0; box-sizing: border-box; }
  html, body { width: 1200px; height: 1000px; overflow: hidden; }
  body {
    background: var(--backdrop);
    font-family: "Arimo", Arial, sans-serif;
    position: relative;
  }
  .card {
    position: absolute;
    left: 290px;
    width: 620px;
    height: 354px;
    overflow: hidden;
    box-shadow: 0 10px 30px rgba(0,0,0,0.35);
  }

  /* Back side */
  .card-back { top: 90px; background: var(--card-dark); }
  .card-back .company-name {
    position: absolute; left: 56px; top: 148px;
    font-size: 42px; font-weight: 400; line-height: 1;
    color: var(--name-light);
  }
  .card-back .tagline {
    position: absolute; right: 44px; top: 52px;
    font-size: 17px; color: var(--accent-orange);
  }
  .card-back .address {
    position: absolute; left: 370px; top: 190px;
    font-size: 15px; line-height: 20px; color: var(--muted-light);
    font-style: normal;
  }
  .card-back .web { margin-top: 12px; color: var(--accent-blue); }

  /* Front side */
  .card-front { top: 520px; background: var(--card-light); }
  .card-front .company-name {
    position: absolute; left: 40px; top: 38px;
    font-size: 40px; font-weight: 400; line-height: 1;
    color: var(--navy);
  }
  .card-front .tagline {
    position: absolute; right: 40px; top: 112px;
    font-size: 18px; color: var(--tag-grey);
  }
  .accent-strip {
    position: absolute; left: 0; top: 150px; width: 230px; height: 5px;
    display: flex;
  }
  .accent-strip span { flex: 1; }
  .accent-strip .s1 { background: var(--accent-blue); }
  .accent-strip .s2 { background: var(--accent-orange); }
  .accent-strip .s3 { background: var(--accent-green); }
  .accent-strip .s4 { background: var(--accent-purple); }
  .name-band {
    position: absolute; left: 230px; right: 0; top: 150px; height: 52px;
    background: linear-gradient(90deg, var(--band-start), var(--band-end));
    padding: 8px 0 0 18px; color: #fff;
  }
  .name-band .person { font-size: 20px; font-weight: 700; }
  .name-band .role { font-size: 13px; color: #d8d8d8; margin-top: 2px; }
  .band-rule {
    position: absolute; left: 230px; right: 0; top: 207px; height: 3px;
    background: var(--band-start);
  }
  .contacts {
    position: absolute; left: 200px; top: 222px;
    font-size: 14.5px; line-height: 19px; color: var(--ink);
  }
  .contacts .gap { height: 12px; }
  .contacts .label { color: var(--accent-orange); }
</style>
</head>
<body>
  <section class="card card-back" aria-label="Business card back">
    <div class="company-name">VELMOsoft</div>
    <p class="tagline">...software built to last</p>
    <address class="address">
      VELMOsoft Solutions AG<br>
      Lindenweg 27<br>
      4410 Liestal<br>
      Switzerland
      <div class="web">www.velmosoft.com</div>
    </address>
  </section>

  <section class="card card-front" aria-label="Business card front">
    <div class="company-name">VELMOsoft</div>
    <p class="tagline">...software built to last</p>
    <div class="accent-strip"><span class="s1"></span><span class="s2"></span><span class="s3"></span><span class="s4"></span></div>
    <div class="name-band">
      <div class="person">Daniel Marek</div>
      <div class="role">CEO</div>
    </div>
    <div class="band-rule"></div>
    <div class="contacts">
      <div>+41 79 5550142</div>
      <div>daniel.marek@velmosoft.com</div>
      <div class="gap"></div>
      <div>+41 44 555 01 20 <span class="label">phone</span></div>
      <div>+41 44 555 01 21 <span class="label">direct</span></div>
      <div>+41 800 555 672 <span class="label">fax</span></div>
    </div>
  </section>
</body>
</html>
```